Delegate Welcome sign

The Copperfield Lodge hotel in Pine Bush NY is welcoming delegations from many different countries during 2019. We want to make a welcome sign about 16:9 ratio about 4 feet high with raised letters. I have attached a background design that we liked and a template with the wording. As you will see I need help with it.

```html
<!DOCTYPE html>
<html lang="en">
<head>
<meta charset="utf-8">
<title>Copperfield Lodge Hotel – Delegate Welcome Sign</title>
<link rel="stylesheet" href="https://fonts.googleapis.com/css2?family=Montserrat:wght@600;700&display=swap">
<style>
  :root {
    --brown: #3a2317;
    --gold: #f8bd42;
    --gold-deep: #f1b03a;
    --white: #ffffff;
  }
  * { margin: 0; padding: 0; box-sizing: border-box; }
  html, body {
    width: 1200px;
    height: 675px;
    overflow: hidden;
    background: var(--brown);
  }
  .sign {
    position: relative;
    width: 1200px;
    height: 675px;
    background: var(--brown);
    font-family: "Montserrat", Arial, sans-serif;
    text-align: center;
    overflow: hidden;
  }
  .sign__line {
    position: absolute;
    left: 0;
    width: 100%;
    line-height: 1;
  }
  .host-name {
    top: 64px;
    font-size: 44px;
    font-weight: 700;
    letter-spacing: 1px;
    color: var(--white);
  }
  .host-verb {
    top: 133px;
    font-size: 48px;
    font-weight: 600;
    color: var(--white);
  }
  .welcome-band {
    position: absolute;
    left: 0;
    top: 207px;
    width: 100%;
    height: 343px;
    background: radial-gradient(ellipse at center, var(--gold) 0%, var(--gold) 55%, var(--gold-deep) 100%);
  }
  .guests {
    font-size: 72px;
    font-weight: 700;
    letter-spacing: 1px;
    color: var(--brown);
  }
  .guests--year { top: 244px; }
  .guests--title { top: 330px; }
  .place {
    font-size: 47px;
    font-weight: 700;
    letter-spacing: 1px;
    color: var(--brown);
  }
  .place--region { top: 430px; }
  .place--state { top: 485px; }
  .hashtag {
    top: 588px;
    font-size: 39px;
    font-weight: 600;
    color: var(--white);
  }
</style>
</head>
<body>
  <main class="sign">
    <p class="sign__line host-name">THE COPPERFIELD LODGE HOTEL</p>
    <p class="sign__line host-verb">welcomes</p>

    <div class="welcome-band" role="img" aria-label="Golden band with a dense leaf and flower pattern"></div>

    <h1 class="sign__line guests guests--year">2019 INTERNATIONAL</h1>
    <h1 class="sign__line guests guests--title">DELEGATES</h1>
    <p class="sign__line place place--region">TO THE HUDSON VALLEY</p>
    <p class="sign__line place place--state">IN NEW YORK</p>

    <p class="sign__line hashtag">#copperfieldlodgehotel</p>
  </main>
</body>
</html>
```